Social Media designs (LinkedIn banner, LinkedIn posts, Instagram)

Hello designers!
We are looking to create some more concepts for our social media identity for a search firm (recruitment company)
I have attached a "brand toolkit" that shows our brand, logo, colour scheme to guide you with regards to colours and identiy.

You will see in the brand toolkit there are some examples of;
- A LinkedIn banner for the company (page 23)
- Social Media posts for LinkedIn and Instagram (page 21)

What we are looking for...

We don't really like the current LinkedIn banner ideas. We would like to see more concepts that look more aesthetically pleasing - the current ideas look quite dull.

We DO like the social media post concepts but we would like to have more templates/options that we can use (similar themes)

We welcome submissions for Social Media designs that we can use with our company branding. Thank you for your work in advance!

```html
<!DOCTYPE html>
<html lang="en">
<head>
<meta charset="UTF-8">
<title>Talent Knows No Borders – Banner</title>
<link href="https://fonts.googleapis.com/css2?family=Manrope:wght@600;700&display=swap" rel="stylesheet">
<style>
  :root {
    --bg: #10231f;
    --ink: #ffffff;
    --accent: #3f8a68;
    --night-1: #070f0d;
    --night-2: #1b2f2b;
    --street-1: #d4d6d5;
    --street-2: #3a3c3c;
  }
  * { margin: 0; padding: 0; box-sizing: border-box; }
  html, body {
    width: 1200px;
    height: 1200px;
    overflow: hidden;
    background: var(--bg);
  }
  .canvas {
    position: relative;
    width: 1200px;
    height: 1200px;
    background: var(--bg);
  }
  .banner {
    position: absolute;
    left: 0;
    top: 451px;
    width: 1200px;
    height: 297px;
  }
  .banner-art {
    position: absolute;
    inset: 0;
    width: 1200px;
    height: 297px;
    display: block;
  }
  .headline {
    position: absolute;
    left: 299px;
    top: 90px;
    font-family: "Manrope", sans-serif;
    font-weight: 700;
    font-size: 55px;
    line-height: 56px;
    letter-spacing: -0.5px;
    color: var(--ink);
    text-transform: uppercase;
  }
  .headline .accent { color: var(--accent); font-weight: 600; }
</style>
</head>
<body>
<div class="canvas">
  <section class="banner">
    <svg class="banner-art" viewBox="0 0 1200 297" xmlns="http://www.w3.org/2000/svg">
      <defs>
        <linearGradient id="nightGrad" x1="0" y1="0" x2="1" y2="0">
          <stop offset="0" stop-color="var(--night-1)"/>
          <stop offset="0.45" stop-color="var(--night-2)"/>
          <stop offset="1" stop-color="var(--night-1)"/>
        </linearGradient>
        <linearGradient id="streetGrad" x1="0" y1="0" x2="0" y2="1">
          <stop offset="0" stop-color="var(--street-1)"/>
          <stop offset="1" stop-color="var(--street-2)"/>
        </linearGradient>
      </defs>
      <polygon class="photo-cathedral" points="0,0 826,0 935,297 0,297" fill="url(#nightGrad)" role="img" aria-label="Dark photo of a domed cathedral seen through glass office buildings"/>
      <polygon class="photo-street" points="826,0 1200,0 1200,297 935,297" fill="url(#streetGrad)" role="img" aria-label="Black and white photo of an empty city street lined with historic buildings"/>
      <g class="accent-stripes" fill="var(--accent)" opacity="0.6">
        <polygon points="826,0 868,0 990,297 935,297"/>
        <polygon points="1095,0 1130,0 1020,297 985,297"/>
        <polygon points="1110,0 1145,0 1200,150 1200,250"/>
      </g>
      <g class="base-bars" fill="var(--accent)">
        <rect x="0" y="283" width="31" height="14"/>
        <rect x="228" y="283" width="474" height="14"/>
      </g>
    </svg>
    <h1 class="headline"><span class="accent">Talent</span> Knows<br>No Borders</h1>
  </section>
</div>
</body>
</html>
```